Rack Cards, Banner, Table Cover

Bright Harbor Teeth Cleaning Powder. Specially formulated by Dr. Holbrook.
I am attaching a file with our artwork for the front of the actual bottle and the back of the bottle. Id like to stay with these colors as well.

Contact Information for Business Card

I'm not actually needing business cards at this time... I need Rack Cards (information cards) to display, a table cover and a banner. We are attending a dental conference and will have an exhibitors booth set up for our product.

```html
<!DOCTYPE html>
<html lang="en">
<head>
<meta charset="utf-8">
<title>Bright Harbor Teeth Cleaning Powder – Rack Card</title>
<link href="https://fonts.googleapis.com/css2?family=Patrick+Hand&family=Roboto+Slab:wght@500;700&display=swap" rel="stylesheet">
<style>
  :root {
    --teal: #1b98a6;
    --tooth-white: #ffffff;
    --tooth-shade: #e9ecee;
    --brand-teal: #1a8f9c;
    --leaf-green: #4ea53a;
    --sky-text: #a9d9ea;
    --band-white: #ffffff;
  }
  html, body {
    margin: 0;
    padding: 0;
    width: 1200px;
    height: 2668px;
    overflow: hidden;
  }
  .rack-card {
    position: relative;
    width: 1200px;
    height: 2668px;
    background: var(--teal);
    overflow: hidden;
  }
  .tooth-illustration {
    position: absolute;
    left: 180px;
    top: 420px;
    width: 988px;
    height: 1940px;
    border-radius: 380px 380px 120px 120px;
    background: linear-gradient(160deg, var(--tooth-white) 70%, var(--tooth-shade) 100%);
  }
  .product-name {
    position: absolute;
    left: 0;
    width: 1200px;
    top: 990px;
    margin: 0;
    text-align: center;
    font-weight: normal;
  }
  .product-name .brand {
    display: block;
    font-family: "Roboto Slab", serif;
    font-weight: 500;
    font-size: 86px;
    letter-spacing: 2px;
    color: var(--brand-teal);
    line-height: 1.1;
  }
  .product-name .product {
    display: block;
    font-family: "Patrick Hand", cursive;
    font-size: 84px;
    color: var(--leaf-green);
    line-height: 1.15;
  }
  .benefits {
    position: absolute;
    left: 0;
    width: 1240px;
    top: 1320px;
    text-align: center;
    font-family: "Patrick Hand", cursive;
    font-size: 70px;
    line-height: 140px;
    color: var(--sky-text);
  }
  .benefits p { margin: 0 0 140px; }
  .dotted-rule {
    position: absolute;
    left: 0;
    width: 1200px;
    height: 0;
    border-top: 8px dotted var(--band-white);
  }
  .dotted-rule.upper { top: 2452px; }
  .dotted-rule.lower { top: 2622px; }
  .formulator-band {
    position: absolute;
    left: 0;
    top: 2484px;
    width: 1200px;
    height: 118px;
    background: var(--band-white);
    display: flex;
    align-items: center;
    justify-content: center;
    font-family: "Roboto Slab", serif;
    font-weight: 700;
    font-size: 54px;
    color: var(--leaf-green);
    margin: 0;
  }
</style>
</head>
<body>
  <main class="rack-card">
    <div class="tooth-illustration" role="img" aria-label="Large white tooth illustration with green sparkles above its left side"></div>

    <h1 class="product-name">
      <span class="brand">BRIGHT HARBOR</span>
      <span class="product">Teeth Cleaning Powder</span>
    </h1>

    <div class="benefits">
      <p>A natural way to help<br>raise oral pH in acidic mouths.</p>
      <p>For tooth brushing and reducing<br>pathogenic bacteria in the mouth.</p>
    </div>

    <div class="dotted-rule upper"></div>
    <p class="formulator-band">Specially formulated by Dr. Holbrook</p>
    <div class="dotted-rule lower"></div>
  </main>
</body>
</html>
```